Need business card design that I can update for new employees and details. Needs to incorporate our logo, be bright and fun (in line with tourism and holidays)
Would like a Map of Western Australia on the front with locations all the caravan parks we own (just purchased Tom Price so please include that as well as others listed on our website).
Famillies
5 Cards -
Victor Pembrook (Director) e: pembrook@kelpiegrove.com.au p: 0491 570 156
Ros Pembrook (Director) e: pembrook@kelpiegrove.com.au p: 0491 570 157
Oliver Halvey (General Manager) e: halvey@kelpiegrove.com.au p: 0491 570 158
Megan Halvey (General Manager) e: halvey@kelpiegrove.com.au p: 0491 570 159
Neil Ashworth (Training and Operations Manager) - e: ashworth@kelpiegrove.com.au p:0491 570 110

```html
<!DOCTYPE html>
<html lang="en">
<head>
<meta charset="utf-8">
<title>Kelpie Grove Business Card</title>
<link href="https://fonts.googleapis.com/css2?family=Roboto:wght@400;500&family=Roboto+Condensed:wght@500&display=swap" rel="stylesheet">
<style>
  :root {
    --backdrop: #2b2b2b;
    --paper: #f1f1f1;
    --teal: #40bac4;
    --sea-green: #6cb9a9;
    --white: #ffffff;
    --ink: #555555;
    --ink-soft: #4a4a4a;
  }
  * { margin: 0; padding: 0; box-sizing: border-box; }
  html, body {
    width: 1200px; height: 960px; overflow: hidden;
    background: var(--backdrop);
    font-family: "Roboto", Arial, sans-serif;
  }
  .canvas { position: relative; width: 1200px; height: 960px; }
  .card {
    position: absolute; width: 600px; height: 343px;
    background: var(--paper); overflow: hidden;
  }
  .card--front { left: 314px; top: 113px; }
  .card--back { left: 311px; top: 472px; }
  .wave { position: absolute; inset: 0; width: 600px; height: 343px; }

  .holder { position: absolute; left: 39px; top: 33px; color: var(--white); }
  .holder__name {
    font-family: "Roboto Condensed", "Arial Narrow", sans-serif;
    font-weight: 500; font-size: 21px; line-height: 24px; letter-spacing: 0.2px;
  }
  .holder__title { font-size: 15px; line-height: 18px; font-weight: 500; margin-top: 2px; margin-left: 1px; }

  .contacts {
    position: absolute; right: 38px; top: 34px; list-style: none;
    color: var(--white); font-size: 14.5px; line-height: 19.5px; text-align: right;
  }
  .contacts li { display: flex; justify-content: flex-end; align-items: center; gap: 6px; }
  .contacts svg { width: 13px; height: 13px; flex: none; }

  .brand { position: absolute; left: 48px; top: 186px; display: flex; flex-direction: column; align-items: center; gap: 12px; width: 222px; }
  .brand__mark { width: 70px; height: 70px; background: var(--teal); }
  .brand__name {
    font-size: 24px; font-weight: 400; letter-spacing: 3px;
    text-transform: uppercase; color: var(--ink);
  }

  .brand--back { left: 0; top: 98px; width: 600px; gap: 16px; }
  .brand--back .brand__mark { width: 100px; height: 100px; }
  .brand--back .brand__name { font-size: 22px; }

  .back-web {
    position: absolute; left: 0; right: 0; top: 293px; text-align: center;
    font-size: 14.5px; letter-spacing: 2.6px; color: var(--ink-soft);
  }
</style>
</head>
<body>
<main class="canvas">

  <section class="card card--front" aria-label="Business card front">
    <svg class="wave" viewBox="0 0 600 343" aria-hidden="true">
      <path fill="var(--sea-green)" d="M0,0 H600 V280 C560,285 500,285 430,255 C350,215 290,132 210,112 C130,95 60,100 0,112 Z"/>
      <path fill="var(--teal)" d="M0,0 H600 V252 C550,258 490,262 420,235 C340,200 280,130 200,110 C130,95 60,100 0,112 Z"/>
      <path fill="none" stroke="var(--white)" stroke-width="2" d="M0,112 C60,100 130,95 200,110 C280,130 340,200 420,235 C490,262 550,258 600,252"/>
    </svg>

    <div class="holder">
      <p class="holder__name">VICTOR PEMBROOK</p>
      <p class="holder__title">DIRECTOR</p>
    </div>

    <ul class="contacts">
      <li>0491 570 156
        <svg viewBox="0 0 24 24" aria-hidden="true"><path fill="#fff" d="M6.6 10.8c1.4 2.8 3.8 5.1 6.6 6.6l2.2-2.2c.3-.3.7-.4 1-.2 1.1.4 2.3.6 3.6.6.6 0 1 .4 1 1V20c0 .6-.4 1-1 1C10.6 21 3 13.4 3 4c0-.6.4-1 1-1h3.5c.6 0 1 .4 1 1 0 1.3.2 2.5.6 3.6.1.3 0 .7-.2 1z"/></svg>
      </li>
      <li>pembrook@kelpiegrove.com.au
        <svg viewBox="0 0 24 24" aria-hidden="true"><rect x="2" y="5" width="20" height="14" rx="1.5" fill="#fff"/><path d="M3 6l9 7 9-7" fill="none" stroke="var(--teal)" stroke-width="1.8"/></svg>
      </li>
      <li>www.kelpiegrove.com.au
        <svg viewBox="0 0 24 24" aria-hidden="true"><circle cx="12" cy="12" r="10" fill="#fff"/><path d="M12 2v20M2 12h20M5 6c4 2 10 2 14 0M5 18c4-2 10-2 14 0" fill="none" stroke="var(--teal)" stroke-width="1.5"/></svg>
      </li>
    </ul>

    <div class="brand">
      <span class="brand__mark" aria-hidden="true"></span>
      <span class="brand__name">Kelpie Grove</span>
    </div>
  </section>

  <section class="card card--back" aria-label="Business card back">
    <div class="brand brand--back">
      <span class="brand__mark" aria-hidden="true"></span>
      <span class="brand__name">Kelpie Grove</span>
    </div>
    <p class="back-web">www.kelpiegrove.com.au</p>
  </section>

</main>
</body>
</html>
```